A new company focused on starting and investing in transformative businesses.

We need a simple and clean website with a few pages. we like marlowvest.com as a starting point. we want the landing page to be very simple with an option to click through on the top right into INVESTOR LOGIN. then we want to be able to scroll down to see more about our company.

Target Market(s)

professional

Coding

Coded - Design and coding required

Number of Pages Required

2 page

Font styles to use
Serif
Sans Serif

Requirements
Must have
• HALVERN BUILDERS logo (attached as a file) on the top with INVESTOR LOGIN as a click through on the right. Please model the click through from marlowvest.com. The description (also written in attached file) should be on the landing page. we do not want to have to scroll to read the description.

Then we can scroll down to read more about Halvern including the mission and the two types of businesses. More is detailed on the attached file called "Halvern Website Syntax"
Should not have
• should not be slow loading with lots of fancy graphics. should not be busy and with too many colors.

```html
<!DOCTYPE html>
<html lang="en">
<head>
<meta charset="utf-8">
<title>Halvern Builders</title>
<link rel="stylesheet" href="https://fonts.googleapis.com/css2?family=EB+Garamond:wght@500;600&family=Barlow+Semi+Condensed:wght@600&family=Montserrat:wght@400;600&family=Barlow:wght@500;600&display=swap">
<style>
:root{
  --brand:#00659c;
  --ink:#111111;
  --muted:#6b6b6b;
  --white:#ffffff;
  --footer:#262626;
  --footer-mid:#3d3d3d;
  --rule:#4a4a4a;
}
*{box-sizing:border-box;margin:0;padding:0}
html,body{width:723px;height:1200px;overflow:hidden;background:var(--white)}
.page{position:relative;width:723px;height:1200px;overflow:hidden;font-family:"Montserrat",sans-serif;color:var(--ink)}
.abs{position:absolute}

.topbar{left:0;top:0;width:723px;height:20px;background:var(--brand)}
.topbar-mail{right:37px;top:5px;display:flex;align-items:center;gap:5px;color:var(--white);font-size:7.5px}
.mail-icon{width:13px;height:9px}

.header{left:0;top:20px;width:723px;height:38px;background:var(--white)}
.brand{left:36px;top:25px;display:flex;align-items:center;gap:7px}
.brand-square{width:30px;height:30px;background:var(--brand)}
.brand-name{font-family:"Barlow",sans-serif;font-weight:600;font-size:13px;line-height:14px;color:var(--ink);letter-spacing:.3px}
.login{left:583px;top:27px;width:104px;height:25px;border-radius:13px;background:var(--ink);display:flex;align-items:center;justify-content:space-between;padding:0 3px 0 8px;color:var(--white);font-family:"Barlow",sans-serif;font-weight:500;font-size:9px;letter-spacing:.2px}
.login-dot{width:20px;height:20px;border-radius:50%;background:var(--white)}

.hero{left:0;top:58px;width:723px;height:390px}
.hero-title{left:37px;top:160px;width:420px;font-family:"EB Garamond",serif;font-weight:600;font-size:21px;line-height:27.5px;color:var(--white)}
.hero-title strong{font-size:25.5px;font-weight:600}

.section-title{font-family:"Barlow Semi Condensed",sans-serif;font-weight:600;color:var(--ink)}
.about-title{left:0;top:487px;width:723px;text-align:center;font-size:18.5px}
.divider{overflow:visible}
.mission{left:0;top:532px;width:723px;text-align:center;font-size:8.4px;line-height:14px;color:var(--muted)}
.mission b{color:var(--brand);font-weight:600}

.photo{border:none}
.types-title{left:385px;top:630px;font-size:16px}
.biz{left:384px;width:290px;display:flex;gap:14px}
.biz-icon{width:46px;height:46px;flex:none}
.biz-name{font-size:11px;color:var(--ink);margin-bottom:3px;font-weight:400}
.biz-text{font-size:7.4px;line-height:11.7px;color:var(--muted)}

.footer{left:0;top:960px;width:723px;height:240px}
.foot-heading{top:1082px;font-size:13.5px;color:var(--white)}
.inquiries{left:37px}
.follow{right:37px}
.foot-mail{left:37px;top:1108px;display:flex;align-items:center;gap:6px;color:var(--white);font-size:7.6px}
.foot-mail .mail-icon{width:17px;height:11px}
.foot-brand{left:308px;top:1084px;display:flex;align-items:center;gap:7px}
.foot-brand .brand-square{background:var(--white);width:28px;height:28px}
.foot-brand .brand-name{color:var(--white);font-weight:500}
.social{left:616px;top:1111px;display:flex;gap:5px}
.social span{width:20px;height:20px;border-radius:50%;background:var(--white);display:block}
.foot-rule{left:36px;top:1165px;width:651px;height:1px;background:var(--rule)}
.copyright{left:0;top:1179px;width:723px;text-align:center;font-size:7px;color:#d0d0d0}
</style>
</head>
<body>
<div class="page">

  <div class="abs topbar"></div>
  <div class="abs topbar-mail">
    <svg class="mail-icon" viewBox="0 0 13 9"><rect width="13" height="9" fill="#fff"/><path d="M0 0l6.5 5L13 0" fill="none" stroke="#00659c" stroke-width="1.2"/></svg>
    nora@halvernbuilders.com
  </div>

  <div class="abs header"></div>
  <div class="abs brand">
    <span class="brand-square"></span>
    <span class="brand-name">HALVERN<br>BUILDERS</span>
  </div>
  <a class="abs login">INVESTOR LOGIN<span class="login-dot"></span></a>

  <svg class="abs hero" viewBox="0 0 723 390" role="img" aria-label="Photo of a woman reading documents at an office desk">
    <defs>
      <linearGradient id="heroTone" x1="0" y1="0" x2="1" y2="0.4">
        <stop offset="0" stop-color="#3c3d40"/>
        <stop offset=".55" stop-color="#4a4a4c"/>
        <stop offset="1" stop-color="#5c5e62"/>
      </linearGradient>
    </defs>
    <polygon points="0,0 723,0 723,323 531,384 204,294 0,312" fill="url(#heroTone)"/>
    <polygon points="0,312 204,294 723,289 723,334 531,384" fill="#ffffff" opacity=".55"/>
  </svg>
  <h1 class="abs hero-title"><strong>Halvern Builders</strong> is an entrepreneurial firm focused on building and growing transformational companies</h1>

  <h2 class="abs section-title about-title">About Company</h2>
  <svg class="abs divider" style="left:318px;top:512px" width="88" height="16" viewBox="0 0 88 16">
    <line x1="0" y1="7" x2="30" y2="7" stroke="#00659c" stroke-width=".8"/>
    <circle cx="43.5" cy="7" r="6.5" fill="none" stroke="#00659c" stroke-width=".8"/>
    <line x1="57" y1="7" x2="87" y2="7" stroke="#00659c" stroke-width=".8"/>
  </svg>
  <p class="abs mission">Our mission is to build <b>meaningful</b> businesses that create <b>enduring</b><br>value by impacting people in a <b>measurable</b> way.</p>

  <svg class="abs photo" style="left:73px;top:628px" width="126" height="135" role="img" aria-label="Photo of hands reviewing financial charts on a wooden desk"><rect width="126" height="135" fill="#6e5440"/><rect width="126" height="135" fill="url(#g1)"/><defs><linearGradient id="g1" x1="0" y1="0" x2="1" y2="1"><stop offset="0" stop-color="#3a2e28"/><stop offset=".6" stop-color="#8a6d55"/><stop offset="1" stop-color="#d8d4cc"/></linearGradient></defs></svg>
  <svg class="abs photo" style="left:217px;top:601px" width="127" height="135" role="img" aria-label="Photo of a smiling business team in an office"><defs><linearGradient id="g2" x1="0" y1="0" x2="0" y2="1"><stop offset="0" stop-color="#c9ccd0"/><stop offset=".5" stop-color="#7d8fa8"/><stop offset="1" stop-color="#3d4352"/></linearGradient></defs><rect width="127" height="135" fill="url(#g2)"/></svg>
  <svg class="abs photo" style="left:73px;top:781px" width="126" height="136" role="img" aria-label="Photo of hands typing on a laptop showing charts"><defs><linearGradient id="g3" x1="0" y1="0" x2="1" y2="1"><stop offset="0" stop-color="#e4e7ea"/><stop offset=".5" stop-color="#9eaab8"/><stop offset="1" stop-color="#4a4d52"/></linearGradient></defs><rect width="126" height="136" fill="url(#g3)"/></svg>
  <svg class="abs photo" style="left:217px;top:755px" width="127" height="135" role="img" aria-label="Photo of a business handshake over a meeting table"><defs><linearGradient id="g4" x1="0" y1="0" x2="1" y2="1"><stop offset="0" stop-color="#5c6068"/><stop offset=".5" stop-color="#c9a58c"/><stop offset="1" stop-color="#e6e4e0"/></linearGradient></defs><rect width="127" height="135" fill="url(#g4)"/></svg>

  <h2 class="abs section-title types-title">Types of businesses</h2>
  <svg class="abs divider" style="left:384px;top:652px" width="52" height="15" viewBox="0 0 52 15">
    <circle cx="7" cy="7" r="6.5" fill="none" stroke="#00659c" stroke-width=".8"/>
    <line x1="21" y1="7" x2="51" y2="7" stroke="#00659c" stroke-width=".8"/>
  </svg>

  <div class="abs biz" style="top:695px">
    <svg class="biz-icon" viewBox="0 0 46 46" aria-hidden="true">
      <rect x="8" y="8" width="30" height="30" rx="4" transform="rotate(45 23 23)" fill="#00659c"/>
      <circle cx="23" cy="19" r="4" fill="none" stroke="#fff" stroke-width="1.2"/>
      <path d="M15 32c0-5 4-8 8-8s8 3 8 8z" fill="none" stroke="#fff" stroke-width="1.2"/>
    </svg>
    <div>
      <h3 class="biz-name">Ground Up</h3>
      <p class="biz-text">Our ground up business applies a proven analytic process to identify value edge, a form of competitive advantage. We architect transformational companies and are deliberate in creating the foundation necessary to lead an industry.</p>
    </div>
  </div>

  <div class="abs biz" style="top:790px">
    <svg class="biz-icon" viewBox="0 0 46 46" aria-hidden="true">
      <rect x="8" y="8" width="30" height="30" rx="4" transform="rotate(45 23 23)" fill="#00659c"/>
      <circle cx="20" cy="20" r="6" fill="none" stroke="#fff" stroke-width="1.3"/>
      <line x1="24.5" y1="24.5" x2="30" y2="30" stroke="#fff" stroke-width="1.8" stroke-linecap="round"/>
    </svg>
    <div>
      <h3 class="biz-name">Special Opportunities</h3>
      <p class="biz-text">We partner with exceptional teams that create value by transforming lives. Our investment focus includes large companies and spin-outs.</p>
    </div>
  </div>

  <svg class="abs footer" viewBox="0 0 723 240" role="img" aria-label="Darkened photo of a desk with papers and a keyboard">
    <polygon points="0,59 192,9 723,85 723,240 0,240" fill="var(--footer-mid)"/>
    <polygon points="0,104 157,75 723,87 723,240 0,240" fill="var(--footer)"/>
  </svg>

  <h3 class="abs foot-heading inquiries" style="font-weight:400">Inquiries</h3>
  <div class="abs foot-mail">
    <svg class="mail-icon" viewBox="0 0 17 11"><rect width="17" height="11" fill="#fff"/><path d="M0 0l8.5 6L17 0" fill="none" stroke="#262626" stroke-width="1.3"/></svg>
    nora@halvernbuilders.com
  </div>

  <div class="abs foot-brand">
    <span class="brand-square"></span>
    <span class="brand-name">HALVERN<br>BUILDERS</span>
  </div>

  <h3 class="abs foot-heading follow" style="font-weight:400">Follow Us</h3>
  <div class="abs social" aria-label="Social links"><span></span><span></span><span></span></div>

  <div class="abs foot-rule"></div>
  <p class="abs copyright">©2021 halvernbuilders-All Right Reserved.</p>
</div>
</body>
</html>
```